High end Sports Bar/ Restaurant Postcard Design

We are a high end sports bar/restaurant in forest hills on Marren street, we have high quality bar food, 24 draft beers, wine on tap and a great selection of whiskeys & scotches.
What we need is a brightly colored postcard that advertises our weekly events. It must be easy to read but eye-catching and full of fun images that will want to make people come in and drink & eat!
We are called Harlow Commons and have a gastropub feel with one entire wall covered in brick but with 9 t.v's all with audio for all sports games. We are definitely a restaurant too so its not all about sports however we will be carrying the TGX & Harbourline Select League Soccer packages.
On the back of the card we would like to advertise our lunch menu is Monday to Friday 10a.m - 3p.m. Dinner is Sunday - Monday 3p.m - 11p.m and Brunch on Saturday & Sunday. Late night bar menu also available Thursday, Friday & Saturday from 11p.m - 1a.m
Address: 41-16 Marren Street, Forest Hills, N.Y 11375 Phone number: 718 555.0143
Updates

Reason: We are extending the deadline to give us time to figure out which design is best for us, thank you all for your participation

Target Market(s)

21 - 45 year olds

Industry/Entity Type

Restaurant

Requirements
Must have
• Each individual days event must be eye-catching yet easy to read.

```html
<!DOCTYPE html>
<html lang="en">
<head>
<meta charset="utf-8">
<title>Harlow Commons – Weekly Events Postcard</title>
<link rel="stylesheet" href="https://fonts.googleapis.com/css2?family=Alfa+Slab+One&family=Yanone+Kaffeesatz:wght@400;500&family=Yellowtail&display=swap">
<style>
:root{
  --ink:#060606;
  --paper:#ffffff;
  --frame:#9a9a9a;
  --purple:#a868ad;
  --green-sun:#6cc064;
  --orange:#f7941d;
  --teal:#1bb3bc;
  --green:#13a04b;
  --violet:#5f56a5;
  --red:#ec1c24;
  --brick:#d1232a;
  --lunch:#1ab3bf;
  --dinner:#1f8fd0;
  --brunch:#ec9523;
  --slab:"Alfa Slab One", serif;
  --cond:"Yanone Kaffeesatz", sans-serif;
  --script:"Yellowtail", cursive;
}
*{margin:0;padding:0;box-sizing:border-box}
html,body{width:783px;height:1200px;overflow:hidden;background:var(--paper)}
.sheet{position:absolute;left:0;top:0;width:877px;height:1352px;transform:scale(.8928,.8876);transform-origin:0 0}
.card{position:absolute;left:23px;width:838px;height:650px;border:1px solid var(--frame);background:var(--paper);overflow:hidden}
.front{top:18px}
.back{top:685px}
.block{position:absolute}
.slab{font-family:var(--slab);color:var(--ink);line-height:1;letter-spacing:2px}
.cond{font-family:var(--cond);color:var(--paper);line-height:1;white-space:nowrap}
.center{text-align:center}

/* front */
.side-bar{left:21px;top:20px;width:54px;height:589px;background:var(--ink)}
.side-red{left:82px;top:20px;width:63px;height:589px;background:var(--red)}
.happy{left:153px;top:20px;width:391px;height:101px;background:var(--purple)}
.sun{left:556px;top:20px;width:259px;height:101px;background:var(--green-sun)}
.happy .slab,.sun .slab{font-size:38px;margin-top:8px}
.happy .cond,.sun .cond{font-size:48px;margin-top:4px}
.small{font-size:.6em}
.name-band{left:21px;top:127px;width:797px;height:98px;background:var(--ink)}
.brand{position:absolute;left:14px;top:32px;font-family:var(--slab);font-size:26px;color:var(--paper);line-height:1;letter-spacing:1px;white-space:nowrap}
.tagline{position:absolute;left:388px;top:12px;font-size:42px;line-height:.95}
.weekly{position:absolute;left:690px;top:14px;font-family:var(--script);font-size:28px;color:var(--red);line-height:.95;text-align:center;transform:rotate(-10deg)}
.day{top:233px;height:391px}
.day .slab{font-size:34px;margin-top:8px;letter-spacing:1px}
.mon{left:154px;width:129px;background:var(--orange)}
.tue{left:289px;width:127px;background:var(--teal)}
.wed{left:423px;width:128px;background:var(--green)}
.thu{left:558px;width:126px;background:var(--violet)}
.fri{left:690px;width:128px;background:var(--red)}
.fri .slab{font-size:32px}
.fri .and{font-size:18px;display:block;margin:2px 0}
.big{font-size:52px}
.mid{font-size:25px}
.note{font-size:19px;line-height:1.2}
.fine{font-family:var(--cond);font-size:15px;line-height:1.2;color:var(--paper)}

/* back */
.back-red{left:20px;top:19px;width:19px;height:609px;background:var(--brick)}
.back-black{left:44px;top:19px;width:26px;height:609px;background:var(--ink)}
.top-red{left:77px;top:19px;width:553px;height:36px;background:var(--brick)}
.addr-band{left:20px;top:61px;width:610px;height:36px;background:var(--ink)}
.addr-band .brand{left:8px;top:8px;font-size:20px}
.addr{position:absolute;right:8px;top:9px;font-family:var(--cond);font-size:21px;font-weight:500;color:var(--red);white-space:nowrap}
.addr b{font-family:var(--slab);font-size:10px;color:var(--paper);font-weight:400;margin-right:6px;letter-spacing:1px}
.phone{position:absolute;left:44px;top:430px;width:26px;height:190px}
.meal{left:78px;width:327px;padding:8px 0 0 12px}
.meal .slab{font-size:26px}
.meal .served{font-family:var(--script);font-size:26px;color:var(--ink);margin-left:6px}
.meal .cond{font-size:27px;margin-top:4px}
.lunch{top:107px;height:82px;background:var(--lunch)}
.dinner{top:201px;height:82px;background:var(--dinner)}
.brunch{top:295px;height:82px;background:var(--brunch)}
.late{top:385px;height:243px;background:var(--violet)}
.late .served{display:block;margin:2px 0 0}
</style>
</head>
<body>
<main class="sheet">
  <section class="card front">
    <div class="block side-bar"></div>
    <div class="block side-red"></div>
    <div class="block happy center">
      <p class="slab">HAPPY HOUR</p>
      <p class="cond">Monday-Friday <span class="small">11 a.m.</span></p>
    </div>
    <div class="block sun center">
      <p class="slab">SUN</p>
      <p class="cond">Karaoke <span class="small">9 p.m.</span></p>
    </div>
    <div class="block name-band">
      <p class="brand">HARLOW COMMONS</p>
      <p class="cond tagline">Sports Bar<br>&amp; Restaurant</p>
      <p class="weekly">Weekly<br>Events</p>
    </div>

    <div class="block day mon center">
      <p class="slab">MON</p>
      <p class="cond" style="font-size:44px;margin-top:8px">$10</p>
      <p class="cond mid" style="margin-top:6px;line-height:1.25">BURGER + BEER<br>OR<br>SALAD + WINE</p>
      <p class="fine" style="margin-top:18px">*Choice of HC<br>Burger, Garden<br>Burger, or HC Chx<br>Sandwich, Any<br>Salad<br>*Chicken or Steak<br>are additional</p>
    </div>
    <div class="block day tue center">
      <p class="slab">TUE</p>
      <p class="cond big" style="margin-top:8px;line-height:1.2">Happy<br>Hour<br>All Day<br>&amp;<br>Night</p>
    </div>
    <div class="block day wed center">
      <p class="slab">WED</p>
      <p class="cond big" style="margin-top:8px;line-height:1.2">Trivia<br>Night!</p>
      <p class="cond note" style="margin-top:22px">Come test your<br>knowledge of<br>irrelevant facts<br>and win a prize!</p>
      <p class="cond" style="font-size:34px;margin-top:30px">8 p.m.</p>
    </div>
    <div class="block day thu center">
      <p class="slab">THU</p>
      <p class="cond big" style="margin-top:8px;line-height:1.2">Ladies<br>Night!</p>
      <p class="cond" style="font-size:27px;margin-top:14px">8 p.m.-close</p>
      <p class="cond note" style="margin-top:34px">Ladies drink ½<br>price all night!</p>
    </div>
    <div class="block day fri center">
      <p class="slab">FRI<span class="and">AND</span>SAT</p>
      <p class="cond" style="font-size:44px;margin-top:6px">LIVE</p>
      <p class="cond" style="font-size:23px">Entertainment</p>
      <p class="cond" style="font-size:29px;margin-top:28px;line-height:1.3">Food &amp; Drink<br>Specials<br>Every<br>Weekend</p>
    </div>
  </section>

  <section class="card back">
    <div class="block back-red"></div>
    <div class="block back-black"></div>
    <div class="block top-red"></div>
    <div class="block addr-band">
      <p class="brand">HARLOW COMMONS</p>
      <p class="addr"><b>ADDRESS</b>41-16 Marren Street Forest Hills, NY&nbsp; 11375</p>
    </div>
    <svg class="phone" viewBox="0 0 26 190" aria-label="Phone 718 555.0143">
      <text transform="translate(18 186) rotate(-90)" font-family="Alfa Slab One, serif" font-size="8" fill="#ffffff">PHONE</text>
      <text transform="translate(20 138) rotate(-90)" font-family="Yanone Kaffeesatz, sans-serif" font-size="20" font-weight="500" fill="#ec1c24">718 555.0143</text>
    </svg>

    <div class="block meal lunch">
      <p><span class="slab">LUNCH</span><span class="served">served</span></p>
      <p class="cond">Monday to Friday 10 a.m. - 3 p.m.</p>
    </div>
    <div class="block meal dinner">
      <p><span class="slab">DINNER</span><span class="served">served</span></p>
      <p class="cond">Sunday - Monday 3 p.m. - 11 p.m.</p>
    </div>
    <div class="block meal brunch">
      <p><span class="slab">BRUNCH</span><span class="served">served</span></p>
      <p class="cond">Saturday &amp; Sunday</p>
    </div>
    <div class="block meal late">
      <p class="slab">LATE NIGHT</p>
      <p class="served">Bar Menu served</p>
      <p class="cond" style="line-height:1.3">Thursday, Friday &amp; Saturday<br>from 11 p.m. - 1 a.m.</p>
    </div>
  </section>
</main>
</body>
</html>
```